Orvex Panel Flyer

I need a flyer designed for our Orvex Panel software service. Basically most of the content that is on the website (orvexpanel.com.au) but I have uploaded a couple of source files as well. Please continue with this blue colour scheme

Target Market(s)

Business owners

Industry/Entity Type

Software

Font styles to use
Sans Serif

Colors
0456a4

Requirements
Must have
• Content from orvexpanel.com.au and similar theme

```html
<!DOCTYPE html>
<html lang="en">
<head>
<meta charset="utf-8">
<title>Orvex Panel Flyer</title>
<link href="https://fonts.googleapis.com/css2?family=Fira+Sans+Condensed:ital,wght@0,300;0,400;0,600;0,700;1,700&family=Open+Sans:wght@400;600;700&display=swap" rel="stylesheet">
<style>
  :root{
    --backdrop:#4aaef5;
    --navy:#18225e;
    --ink:#0f1a3f;
    --brand:#0456a4;
    --sky:#3d95e3;
    --sky-light:#5fb0f0;
    --white:#ffffff;
    --text-dark:#2c3440;
    --caption:#2f63b8;
  }
  *{box-sizing:border-box;margin:0;padding:0}
  html,body{width:1200px;height:813px;overflow:hidden}
  body{background:var(--backdrop);font-family:"Open Sans",sans-serif;position:relative}

  .flyer{position:absolute;left:315px;top:10px;width:570px;height:793px;background:var(--white);overflow:hidden;box-shadow:0 6px 24px rgba(0,0,0,.18)}

  /* header */
  .hero{position:absolute;left:0;top:0;width:570px;height:300px}
  .hero-bg{position:absolute;inset:0}
  .hero-photo{position:absolute;left:0;top:0;width:570px;height:300px;background:linear-gradient(100deg,#1b2463 0%,#26347e 40%,#3b4fa3 65%,#6f86c6 100%)}
  .hero-shade{position:absolute;left:0;top:0;width:270px;height:300px;background:linear-gradient(90deg,rgba(12,18,52,.92),rgba(20,30,80,.55))}
  .brand{position:absolute;left:26px;top:28px;color:var(--white);display:flex;align-items:center;gap:10px}
  .brand-mark{width:16px;height:16px;background:var(--sky-light)}
  .brand-name{font-family:"Fira Sans Condensed",sans-serif;font-weight:700;font-size:34px;letter-spacing:1px;text-transform:uppercase;line-height:1}
  .about{position:absolute;left:24px;top:100px;width:222px;color:var(--white);text-align:center}
  .about h2{font-family:"Fira Sans Condensed",sans-serif;font-weight:700;font-size:15px;letter-spacing:.5px;margin-bottom:6px}
  .about p{font-size:8.4px;line-height:1.45}

  .trial{position:absolute;right:0;top:236px;font-family:"Fira Sans Condensed",sans-serif;font-style:italic;font-weight:700;font-size:26px;color:var(--white);letter-spacing:.5px;padding-right:22px;text-transform:uppercase}

  /* features */
  .features{position:absolute;left:0;top:300px;width:570px;height:120px;background:var(--sky);display:grid;grid-template-columns:repeat(4,1fr);gap:14px;padding:14px 22px 0}
  .feature{color:var(--white)}
  .feature-title{display:flex;align-items:center;gap:6px;font-size:11.5px;font-weight:600;margin-bottom:6px;color:var(--ink)}
  .feature-title svg{width:14px;height:14px;flex:none}
  .feature p{font-size:8.2px;line-height:1.45;color:#0e2550}

  /* showcase */
  .showcase{position:absolute;left:0;top:420px;width:570px;height:352px;display:grid;grid-template-columns:1fr 1fr;grid-template-rows:1fr 1fr;column-gap:26px;row-gap:10px;padding:18px 26px 14px}
  .item{display:flex;flex-direction:column;gap:6px}
  .screens{height:92px;border-radius:6px;background:linear-gradient(135deg,#2d3340 0%,#4b5566 45%,#c9d1de 46%,#eef2f7 100%)}
  .screens.table{background:linear-gradient(135deg,#9aa4b3 0%,#e7ebf1 40%,#f3c27a 55%,#8fce8a 70%,#eef2f7 100%)}
  .item h3{font-family:"Fira Sans Condensed",sans-serif;font-weight:400;font-size:15px;color:var(--caption);text-transform:uppercase;line-height:1.1}
  .item p{font-size:8.6px;color:var(--text-dark);line-height:1.4}
  .item.reverse{flex-direction:column-reverse;justify-content:flex-end}

  .footer-band{position:absolute;left:0;bottom:0;width:570px;height:21px;background:var(--brand)}
</style>
</head>
<body>
  <main class="flyer">
    <section class="hero">
      <div class="hero-photo" role="img" aria-label="Photo of a businessman thinking at his desk by a window"></div>
      <div class="hero-shade"></div>
      <svg class="hero-bg" width="570" height="300" viewBox="0 0 570 300" aria-hidden="true">
        <polygon points="0,248 290,248 330,205 570,205 570,300 0,300" fill="#3d95e3"/>
      </svg>
      <div class="brand">
        <span class="brand-mark"></span>
        <span class="brand-name">Orvex Panel</span>
      </div>
      <div class="about">
        <h2>ABOUT US</h2>
        <p>We specialise in providing reporting and staff performance management tools to the Nexa Licensed Store (NLS) channel. With our Orvex Panel service, our aim is to help you boost performance in your teams and increase efficiency by providing comprehensive reporting and performance management tools that help you keep your finger on the pulse of your business.</p>
      </div>
      <div class="trial">Contact us for a free trial</div>
    </section>

    <section class="features">
      <div class="feature">
        <div class="feature-title">
          <svg viewBox="0 0 14 14"><path d="M2 12 L12 2 M6 2 H12 V8" stroke="#0f1a3f" stroke-width="1.5" fill="none"/></svg>
          Performance
        </div>
        <p>Less time collecting data, more time coaching your team. Orvex Panel has been proven to shave precious hours out of a manager's day.</p>
      </div>
      <div class="feature">
        <div class="feature-title">
          <svg viewBox="0 0 14 14"><rect x="3.5" y="1" width="7" height="12" rx="1.2" stroke="#0f1a3f" stroke-width="1.3" fill="none"/><circle cx="7" cy="11" r=".8" fill="#0f1a3f"/></svg>
          Mobile friendly
        </div>
        <p>All our reports are fully optimised to be viewed on any platform including smartphones, tablets and PCs.</p>
      </div>
      <div class="feature">
        <div class="feature-title">
          <svg viewBox="0 0 14 14"><rect x="1" y="3" width="12" height="8" stroke="#0f1a3f" stroke-width="1.3" fill="none"/><path d="M1 3 L7 8 L13 3" stroke="#0f1a3f" stroke-width="1.3" fill="none"/></svg>
          Responsive
        </div>
        <p>We are always on top of the current priorities in the channel and respond quickly to give you the insights you need to be proactive and win!</p>
      </div>
      <div class="feature">
        <div class="feature-title">
          <svg viewBox="0 0 14 14"><circle cx="5" cy="8" r="3.5" stroke="#0f1a3f" stroke-width="1.3" fill="none"/><circle cx="10" cy="4.5" r="2.5" stroke="#0f1a3f" stroke-width="1.3" fill="none"/></svg>
          Customisable
        </div>
        <p>We offer a range of customised reporting solutions including traffic reporting, commission tracking, inventory management and just about anything else.</p>
      </div>
    </section>

    <section class="showcase">
      <div class="item">
        <div class="screens" role="img" aria-label="Laptop, tablet and phone showing sales charts"></div>
        <h3>Know your numbers.</h3>
        <p>Simple and interactive reports that highlight the main opportunities in your sales team.</p>
      </div>
      <div class="item">
        <div class="screens table" role="img" aria-label="Two tablets showing colour-coded report tables"></div>
        <h3>Customer experience insights.</h3>
        <p>Gain brilliant insights into the customer experience through a range of reports that breath life into your NPS and RAD data.</p>
      </div>
      <div class="item">
        <div class="screens" role="img" aria-label="Laptop and tablet showing target dashboards"></div>
      </div>
      <div class="item">
        <h3>Custom built solutions.</h3>
        <p>We offer a wide range of customised reporting solutions including staff commission trackers, live BOH TV screens and team product targets.</p>
      </div>
    </section>

    <div class="footer-band"></div>
  </main>
</body>
</html>
```